Business Card Design Project

I have just chosen a logo and would now like this designed onto a business card for my hair salon. I would like it to be classy not to busy and have a wow factor when people look at them
Has to Include on card:
Logo Design
And business details below
Kellie-ann Drummond (owner)
0482 736 219
Rdw@vomblet.com.au
71 Willowmere Rise Corvin Cove
Logo is now attached please provide designs
Hair

```html
<!DOCTYPE html>
<html lang="en">
<head>
<meta charset="utf-8">
<title>Lumen Hair Studio – Business Card</title>
<link rel="stylesheet" href="https://fonts.googleapis.com/css2?family=Cinzel:wght@500&family=Parisienne&display=swap">
<style>
  :root {
    --page: #e8e6e3;
    --card-black: #050505;
    --hair-light: #b9bcc0;
    --hair-mid: #6d7176;
    --hair-dark: #1c1d20;
    --skin: #e9c2ad;
    --brand-pink: #e0307a;
    --accent-teal: #2c6f80;
    --text-white: #f4f4f4;
    --line-tint: #0e1d1a;
  }
  * { box-sizing: border-box; margin: 0; padding: 0; }
  html, body {
    width: 1200px;
    height: 900px;
    overflow: hidden;
    background: var(--page);
  }
  .business-card {
    position: absolute;
    left: 100px;
    top: 133px;
    width: 1000px;
    height: 633px;
    border-radius: 42px;
    overflow: hidden;
    background: var(--card-black);
    box-shadow: 0 10px 30px rgba(0,0,0,0.25);
  }
  .hero-photo {
    position: absolute;
    inset: 0;
    background:
      radial-gradient(ellipse 22% 30% at 36% 52%, var(--skin) 0%, #d9a58e 60%, transparent 100%),
      linear-gradient(100deg, var(--hair-dark) 0%, var(--hair-mid) 22%, var(--hair-light) 38%, var(--hair-mid) 55%, var(--hair-light) 75%, var(--hair-mid) 90%, var(--hair-dark) 100%);
  }
  .info-panel {
    position: absolute;
    left: 510px;
    top: 0;
    width: 440px;
    height: 100%;
    background: var(--card-black);
    color: var(--text-white);
    text-align: center;
  }
  .brand-name {
    position: absolute;
    top: 10px;
    width: 100%;
    font-family: "Cinzel", serif;
    font-weight: 500;
    color: var(--brand-pink);
    line-height: 1.05;
  }
  .brand-name .line-large { display: block; font-size: 62px; letter-spacing: 1px; }
  .brand-name .line-small { display: block; font-size: 40px; letter-spacing: 1px; }
  .script {
    position: absolute;
    left: 0;
    width: 100%;
    font-family: "Parisienne", cursive;
    white-space: nowrap;
  }
  .tint { display: inline-block; background: var(--line-tint); padding: 0 10px; }
  .owner-name { top: 190px; font-size: 42px; }
  .owner-role { top: 250px; font-size: 30px; }
  .star-mark { position: absolute; left: 185px; top: 320px; width: 70px; height: 68px; }
  .phone { top: 415px; font-size: 38px; letter-spacing: 2px; }
  .email { top: 468px; font-size: 32px; }
  .address { top: 528px; font-size: 30px; }
</style>
</head>
<body>
  <div class="business-card">
    <div class="hero-photo" role="img" aria-label="Photo of a woman in profile with long glossy black hair flowing back"></div>
    <div class="info-panel">
      <div class="brand-name">
        <span class="line-large">LUMEN</span>
        <span class="line-small">HAIR STUDIO</span>
      </div>
      <p class="script owner-name"><span class="tint">Kellie-ann Drummond</span></p>
      <p class="script owner-role"><span class="tint">(owner)</span></p>
      <svg class="star-mark" viewBox="0 0 100 96" aria-hidden="true">
        <polygon fill="var(--accent-teal)" points="50,0 61.8,36.3 100,36.3 69.1,58.8 80.9,95.1 50,72.7 19.1,95.1 30.9,58.8 0,36.3 38.2,36.3"/>
      </svg>
      <p class="script phone"><span class="tint">0482 736 219</span></p>
      <p class="script email"><span class="tint">Rdw@vomblet.com.au</span></p>
      <p class="script address"><span class="tint">71 Willowmere Rise Corvin Cove</span></p>
    </div>
  </div>
</body>
</html>
```